Paint Your Own Pottery Studio needs a Menu Design

I'm about to open my "paint your own pottery" studio on December 14th!! I would like to offer a menu of sorts for customers to peruse when they enter.

A couple of menu ideas are this:

#1: Regular session: purchase bisqueware and studio session @ regular rates ($5 for the first 50 minutes and $2 for each additional hour)

#2: Purchase 10 studio hours, get 2 free + 15% off any bisqueware painted during these sessions

#3: Purchase 5 pieces of bisqueware (full price) and the first 5 hours of studio time, get unlimited subsequent studio hours for those 5 pieces.

I hope to offer anywhere from 6-8 menu items.

The studio is located on what used to be the sun porch of an old farmhouse, the house my grandfather and great-grandfather built 100 years ago. The studio has a glorious view of the York River on the chesapeake bay in Virginia. Please see my website info page for more info (www.maplehollowclay.com).

The studio itself has an industrial + farmhouse vibe to it with only white and dark grey/blue for colors (the colors in my logo). The shelving that will be displaying the unpainted pottery (bisqueware) uses industrial pipe as supports and the wood shelves themselves are stained a dark espresso color. The studio is in the process of being organized, but I will upload some photos for reference.

Target Market(s)

women: 18-65. I plan to have both ladies nights with wine as well as kids birthday parties. Many people will come to make gifts as well.

Industry/Entity Type

Paint

Font styles to use
Serif

Requirements
Must have
• A vibe that matches the feel of the interior design of the studio. Clean lines, farmhouse with industrial/modern updates.

```html
<!DOCTYPE html>
<html lang="en">
<head>
<meta charset="utf-8">
<title>Maple Hollow Clay Co — Studio Menu</title>
<link rel="stylesheet" href="https://fonts.googleapis.com/css2?family=EB+Garamond:ital,wght@0,400;0,500;1,400&family=Libre+Baskerville&display=swap">
<style>
  :root {
    --slate: #66777d;
    --navy: #464d5b;
    --ink: #2f3440;
    --paper: #ffffff;
    --line-light: #6f7f86;
    --muted: #8a939c;
  }
  * { margin: 0; padding: 0; box-sizing: border-box; }
  html, body { width: 1200px; height: 927px; overflow: hidden; background: var(--slate); }
  .menu {
    position: relative; width: 1200px; height: 927px; background: var(--slate);
    font-family: "EB Garamond", Georgia, serif; color: var(--ink);
  }
  .sheet { position: absolute; left: 23px; top: 25px; width: 789px; height: 887px; background: var(--paper); overflow: hidden; }
  .side-strip { position: absolute; left: 1157px; top: 25px; width: 43px; height: 887px; background: var(--paper); }
  .bowls-photo {
    position: absolute; left: 0; top: 511px; width: 213px; height: 376px;
    background: radial-gradient(ellipse at 30% 60%, #e4e6e8 0%, #f1f2f3 45%, rgba(255,255,255,0) 75%);
  }
  .brand {
    position: absolute; left: 82px; top: 110px;
    font-family: "Libre Baskerville", Georgia, serif; font-size: 14px; letter-spacing: 1px;
    color: var(--navy); line-height: 1.6; display: flex; align-items: center; gap: 8px; white-space: nowrap;
  }
  .brand-dot { width: 10px; height: 10px; border-radius: 50%; background: var(--navy); flex: none; }
  .title {
    position: absolute; left: 248px; top: 70px; font-family: "Libre Baskerville", Georgia, serif;
    font-weight: 400; font-size: 31px; letter-spacing: 0; color: var(--navy); white-space: nowrap;
  }
  .subtitle { position: absolute; left: 312px; top: 113px; font-style: italic; font-size: 30px; color: var(--muted); white-space: nowrap; }
  .head-rule { position: absolute; left: 56px; top: 170px; width: 756px; height: 5px; background: var(--navy); }
  .intro { position: absolute; left: 0; width: 812px; top: 190px; text-align: center; font-style: italic; font-size: 27px; padding-left: 20px; color: var(--ink); }
  .col-divider { position: absolute; left: 413px; top: 247px; width: 3px; height: 500px; background: var(--navy); }
  .package { position: absolute; width: 345px; }
  .package .num {
    position: absolute; left: 0; font-family: "Libre Baskerville", Georgia, serif; font-size: 44px;
    color: var(--ink); border-bottom: 3px solid var(--navy); width: 64px; text-align: center; line-height: 1.15;
  }
  .package .num small { font-size: 34px; vertical-align: 8px; }
  .package p { margin-left: 74px; font-size: 21px; line-height: 25.5px; color: var(--ink); white-space: nowrap; }
  .special {
    position: absolute; left: 56px; top: 786px; width: 716px; height: 87px; background: var(--navy);
    color: var(--paper); display: flex; align-items: center; border: 4px solid var(--paper); outline: 3px solid var(--navy);
  }
  .special-label { font-family: "Libre Baskerville", Georgia, serif; font-size: 19px; line-height: 1.15; width: 165px; padding-left: 24px; }
  .special-label span { font-size: 23px; }
  .special-offer { font-size: 25px; white-space: nowrap; }
  .events { position: absolute; left: 812px; top: 25px; width: 345px; height: 887px; background: var(--navy); }
  .events .rail { position: absolute; top: 0; width: 3px; height: 100%; background: var(--line-light); }
  .events .band { position: absolute; left: 0; top: 148px; width: 388px; height: 6px; background: var(--line-light); }
  .events h2 {
    position: absolute; left: 0; width: 100%; top: 55px; text-align: center; font-weight: 400;
    font-family: "Libre Baskerville", Georgia, serif; font-size: 36px; line-height: 42px; color: var(--paper);
  }
  .event { position: absolute; left: 0; width: 100%; top: 190px; text-align: center; color: var(--paper); }
  .event h3 { font-weight: 400; font-style: italic; font-size: 27px; margin-bottom: 2px; }
  .event p { font-size: 20px; line-height: 25.5px; }
  .pots-photo {
    position: absolute; left: 0; top: 693px; width: 345px; height: 194px;
    background: linear-gradient(135deg, #e9d4cf 0%, #f3ece8 45%, #f0e1d6 70%, #d9dcdf 100%);
    clip-path: polygon(10% 28%, 40% 22%, 60% 30%, 72% 6%, 88% 0%, 100% 10%, 100% 100%, 0 100%, 0 40%);
  }
</style>
</head>
<body>
<main class="menu">
  <section class="sheet">
    <div class="bowls-photo" role="img" aria-label="Stacked white painted pottery bowls with red dots"></div>
  </section>
  <div class="side-strip"></div>

  <div class="brand"><span class="brand-dot"></span><span>MAPLE HOLLOW<br>CLAY CO</span></div>
  <h1 class="title">WELCOME TO THE STUDIO!</h1>
  <p class="subtitle">What would you like to do today?</p>
  <div class="head-rule"></div>
  <p class="intro">Choose from a variety of packages</p>
  <div class="col-divider"></div>

  <article class="package" style="left:56px;top:253px"><div class="num" style="top:34px"><small>#</small>1</div><p>Regular session: purchase<br>bisqueware and studio session<br>@ regular rates ($5 for the first<br>50 minutes and $2 for each<br>additional hour)</p></article>
  <article class="package" style="left:56px;top:396px"><div class="num" style="top:6px"><small>#</small>2</div><p>Purchase 10 studio hours, get 2<br>free + 15% off any bisqueware<br>painted during these sessions</p></article>
  <article class="package" style="left:56px;top:489px"><div class="num" style="top:30px"><small>#</small>3</div><p>Purchase 5 pieces of bisqueware<br>(full price) and the first 5 hours<br>of studio time, get unlimited<br>subsequent studio hours for<br>those 5 pieces.</p></article>
  <article class="package" style="left:56px;top:633px"><div class="num" style="top:30px"><small>#</small>4</div><p>Purchase 5 pieces of bisqueware<br>(full price) and the first 5 hours<br>of studio time, get unlimited<br>subsequent studio hours for<br>those 5 pieces.</p></article>

  <article class="package" style="left:428px;top:253px"><div class="num" style="top:34px"><small>#</small>5</div><p>Regular session: purchase<br>bisqueware and studio session<br>@ regular rates ($5 for the first<br>50 minutes and $2 for each<br>additional hour)</p></article>
  <article class="package" style="left:428px;top:396px"><div class="num" style="top:6px"><small>#</small>6</div><p>Purchase 10 studio hours, get 2<br>free + 15% off any bisqueware<br>painted during these sessions</p></article>
  <article class="package" style="left:428px;top:489px"><div class="num" style="top:30px"><small>#</small>7</div><p>Purchase 5 pieces of bisqueware<br>(full price) and the first 5 hours<br>of studio time, get unlimited<br>subsequent studio hours for<br>those 5 pieces.</p></article>
  <article class="package" style="left:428px;top:633px"><div class="num" style="top:30px"><small>#</small>8</div><p>Purchase 5 pieces of bisqueware<br>(full price) and the first 5 hours<br>of studio time, get unlimited<br>subsequent studio hours for<br>those 5 pieces.</p></article>

  <aside class="special">
    <div class="special-label">DECEMBER<br><span>SPECIAL</span></div>
    <div class="special-offer">All Holiday Bisqueware – Buy 2 get the 3rd for 1/2 off!</div>
  </aside>

  <section class="events">
    <div class="rail" style="left:22px"></div>
    <div class="rail" style="left:323px"></div>
    <div class="band"></div>
    <h2>UPCOMING<br>EVENTS</h2>
    <div class="event">
      <h3>– Ladies Night –</h3>
      <p>January xx, 6-8<br>Grab your girlfriends and book<br>your seats today!</p>
    </div>
    <div class="pots-photo" role="img" aria-label="Hand-painted white vases with pink, orange and charcoal leaf designs"></div>
  </section>
</main>
</body>
</html>
```